Party Favors and Decorations Business Needs A Business Card Design

We are in need of a Logo design and business card design for a new small business called Lark Meadow Designs. We create party decorations and favours for Bridal Showers, Baby Showers, Weddings Birthdays etc. This is a very personalized service based on Clients theme, colour, and style. We are looking for a high end elegant look. I have attached a file to the style I like including the type of paper.

Target Market(s)

women, young adults, expectant mothers, mothers

Industry/Entity Type

Small Business

Contact Information for Business Card

Lark Meadow Designs Fernbrook Vale 519-608-1942 larkmeadowdesigns.ca dana@larkmeadowparties.com find us on Friendlink

Logo Text

Lark Meadow Designs

Font styles to use
Script

Requirements
Must have
• Name, email, web address, phone number
Should not have
• cutesy graphics

```html
<!DOCTYPE html>
<html lang="en">
<head>
<meta charset="utf-8">
<title>Lark Meadow Designs — Business Card</title>
<link rel="stylesheet" href="https://fonts.googleapis.com/css2?family=Great+Vibes&family=Cormorant+Garamond:wght@400&display=swap">
<style>
  :root {
    --backdrop: #e3959a;
    --card: #ffffff;
    --blush: #f08f98;
    --blush-pale: #fbe4e6;
    --ink: #4a3f42;
    --card-shadow: rgba(120, 50, 56, 0.28);
  }
  * { box-sizing: border-box; margin: 0; padding: 0; }
  html, body {
    width: 1200px;
    height: 814px;
    overflow: hidden;
    background: var(--backdrop);
  }
  .sheet {
    position: relative;
    width: 1200px;
    height: 814px;
    display: flex;
    align-items: center;
    justify-content: center;
    gap: 60px;
  }
  .card {
    position: relative;
    width: 520px;
    height: 298px;
    background: var(--card);
    box-shadow: 0 14px 30px var(--card-shadow);
    overflow: hidden;
  }

  /* Front: wordmark */
  .card--front {
    display: flex;
    align-items: center;
    justify-content: center;
  }
  .wordmark {
    display: flex;
    align-items: center;
    gap: 14px;
  }
  .wordmark__name {
    font-family: "Great Vibes", cursive;
    font-size: 50px;
    line-height: 1;
    color: var(--blush);
    white-space: nowrap;
  }
  .wordmark__dot {
    width: 18px;
    height: 18px;
    border-radius: 50%;
    background: var(--blush);
  }

  /* Back: contact details */
  .card--back .bloom-area {
    position: absolute;
    left: -70px;
    top: -120px;
    width: 360px;
    height: 360px;
    border-radius: 50%;
    background: var(--blush-pale);
  }
  .contact {
    position: absolute;
    left: 236px;
    top: 78px;
    width: 266px;
    color: var(--ink);
  }
  .contact__heading {
    display: flex;
    align-items: center;
    gap: 10px;
  }
  .contact__dot {
    width: 12px;
    height: 12px;
    border-radius: 50%;
    background: var(--blush);
    flex: none;
  }
  .contact__name,
  .contact__line {
    font-family: "Great Vibes", cursive;
    font-size: 18px;
    line-height: 1.3;
    white-space: nowrap;
  }
  .contact__phone {
    font-family: "Cormorant Garamond", serif;
    font-size: 20px;
    letter-spacing: 2px;
    line-height: 1.2;
    margin: 2px 0 4px;
  }
</style>
</head>
<body>
  <main class="sheet">
    <section class="card card--front" aria-label="Business card front">
      <div class="wordmark">
        <span class="wordmark__name">Lark Meadow Designs</span>
        <span class="wordmark__dot" aria-hidden="true"></span>
      </div>
    </section>

    <section class="card card--back" aria-label="Business card back">
      <div class="bloom-area" role="img" aria-label="Large faint blush flower decoration"></div>
      <div class="contact">
        <div class="contact__heading">
          <p class="contact__name">Lark Meadow Designs, Fernbrook Vale</p>
          <span class="contact__dot" aria-hidden="true"></span>
        </div>
        <p class="contact__phone">519-608-1942</p>
        <p class="contact__line">larkmeadowdesigns.ca</p>
        <p class="contact__line">dana@larkmeadowparties.com</p>
        <p class="contact__line">find us on Friendlink</p>
      </div>
    </section>
  </main>
</body>
</html>
```